Advanced Therapeutic Massage Therapist

I need a business card advertising my massage services as an advanced therapeutic massage therapist. I offer advanced therapeutic massage, swedish and deep tissue. I want to create a simple, professional and feminine card. I like bright colours and creativity.

I prefer a bold and experimental approach rather than something status-quo. A card to suggest therapeutic healing through dynamic massage. Motifs, shapes or layout which suggest movement and flow.
Updates

Target Market(s)

Everybody!

Industry/Entity Type

Health And Wellness

Contact Information for Business Card

The card should include:
My name, logo, services offered and my contact details.

Aoibhín Delaney
Massage Therapist

- Swedish - Deep Tissue - Advanced Therapeutic

Phone: (+353) 87 261 9043
Email: regenerate@aoibhindelaney-example.com
Website: www.aoibhindelany-example.com

Font styles to use
Serif
Sans Serif
Decorative
Script

Colors

Designer to choose colors to be used in the design.

Requirements
Must have
• An example may contain something like this, yet concise:
• "Aoibhín Delaney
• Massage Therapist
• - Swedish - Deep Tissue - Advanced Therapeutic"
Nice to have
• This sentence is optional:
• Imagery such as a logo or symbol. I have attached a file containing a logo I had produced however the name is incorrect now as it is "Aoibhín" not "Evie". It could be edited to change it to Aoibhín.
• I have sent the file as .psd .jpg. .pdf and .png
• I like when the card conveys energy, movement, pressure points, flow etc.
• I just like the designer to follow their own style and ideas. I like bright colours but must have a lot of a base colour to offset it. I really prefer them to follow their own inspiration. That is my preference.
Should not have
• Pine trees, non-native trees to Britain and Ireland, exotic flowers or animals that are not native to Britain and Ireland.
• I don't like brown as the background colour of the card.
• The cars shouldn't look like a wedding invitation i.e too many floral type designs.

```html
<!DOCTYPE html>
<html lang="en">
<head>
<meta charset="utf-8">
<title>Aoibhín Delaney – Massage Therapist Business Card</title>
<link rel="stylesheet" href="https://fonts.googleapis.com/css2?family=Parisienne&family=Raleway:wght@400;500;600&family=Cormorant+Garamond:wght@500&display=swap">
<style>
  :root {
    --backdrop: #111111;
    --card-white: #ffffff;
    --mint: #a8dcc5;
    --mint-light: #cdeee3;
    --aqua-wash: #bfe6e4;
    --rust: #a4532e;
    --charcoal: #3a3a3a;
    --logo-teal: #9fd6cf;
    --logo-gold: #c9a55a;
  }
  * { box-sizing: border-box; margin: 0; padding: 0; }
  html, body {
    width: 1200px; height: 1000px; overflow: hidden;
    background: var(--backdrop);
  }
  .canvas {
    position: relative; width: 1200px; height: 1000px;
    display: flex; align-items: center; justify-content: center; gap: 40px;
  }
  .card {
    width: 540px; height: 310px; border-radius: 24px;
    position: relative; overflow: hidden;
    box-shadow: 0 10px 24px rgba(0,0,0,0.5);
  }

  /* Front */
  .card-front {
    background: var(--card-white);
    display: flex; flex-direction: column; align-items: center; justify-content: center;
  }
  .logo-mark { width: 126px; height: 126px; margin-bottom: 4px; }
  .brand-name {
    font-family: "Parisienne", cursive; font-weight: 400;
    font-size: 34px; color: var(--rust); line-height: 1.1;
  }
  .brand-role {
    font-family: "Raleway", sans-serif; font-weight: 600;
    font-size: 14px; color: var(--charcoal); letter-spacing: 0.3px;
  }

  /* Back */
  .card-back {
    background: linear-gradient(180deg, var(--mint-light) 0%, var(--aqua-wash) 30%, var(--mint-light) 100%);
  }
  .contact-row {
    position: absolute; font-family: "Raleway", sans-serif; font-weight: 500;
    font-size: 15px; color: var(--charcoal);
    display: flex; align-items: center; gap: 8px;
  }
  .contact-phone { top: 16px; left: 22px; }
  .contact-email { top: 52px; right: 22px; }
  .contact-row svg { width: 13px; height: 13px; fill: var(--rust); }
  .services-band {
    position: absolute; left: 0; right: 0; top: 80px; height: 178px;
    background: var(--mint);
    display: flex; flex-direction: column; align-items: center; justify-content: center;
  }
  .service {
    font-family: "Cormorant Garamond", serif; font-weight: 500;
    font-size: 30px; color: var(--rust); line-height: 1.12;
  }
  .tagline {
    position: absolute; left: 0; right: 0; bottom: 18px; text-align: center;
    font-family: "Raleway", sans-serif; font-weight: 400;
    font-size: 13px; color: var(--rust);
  }
</style>
</head>
<body>
<main class="canvas">
  <section class="card card-front">
    <svg class="logo-mark" viewBox="0 0 126 126" role="img" aria-label="Brand logo area: round teal and gold emblem">
      <defs>
        <radialGradient id="logoFill" cx="50%" cy="50%" r="50%">
          <stop offset="0%" stop-color="#cdeee9"/>
          <stop offset="75%" stop-color="var(--logo-teal)"/>
          <stop offset="100%" stop-color="var(--logo-gold)"/>
        </radialGradient>
      </defs>
      <circle cx="63" cy="63" r="60" fill="url(#logoFill)"/>
    </svg>
    <h1 class="brand-name">Aoibhín Delaney</h1>
    <p class="brand-role">Massage Therapist</p>
  </section>

  <section class="card card-back">
    <p class="contact-row contact-phone">
      <svg viewBox="0 0 24 24" aria-hidden="true"><path d="M6.6 10.8a15.1 15.1 0 0 0 6.6 6.6l2.2-2.2a1 1 0 0 1 1-.25 11.4 11.4 0 0 0 3.6.57 1 1 0 0 1 1 1V20a1 1 0 0 1-1 1A17 17 0 0 1 3 4a1 1 0 0 1 1-1h3.5a1 1 0 0 1 1 1c0 1.25.2 2.45.57 3.57a1 1 0 0 1-.25 1z"/></svg>
      (+353) 87 261 9043
    </p>
    <p class="contact-row contact-email">
      <svg viewBox="0 0 24 24" aria-hidden="true"><path d="M2 5h20v14H2z M2 5l10 8 10-8" stroke="#fff" stroke-width="1.5"/></svg>
      aoibhinmassage@example.com
    </p>
    <div class="services-band">
      <p class="service">Swedish</p>
      <p class="service">Deep Tissue</p>
      <p class="service">Advanced Therapeutic</p>
    </div>
    <p class="tagline">Fully qualified, specialising in advanced therapeutic and deep tissue massage.</p>
  </section>
</main>
</body>
</html>
```